Bref créative
Modern Business Name Card for IT Company
qLumio Sdn Bhd
Simple
Marissa Tanaka
Senior Manager
Lot C-17, 5B Floor,
8 Kilner Plaza,
No. 7, Jalan 24/6
47810 Petaling Jaya
Selangor, Malaysia
marissa@qlumiomarketing.example
www.qlumiomarketing.example
2187605-K
Kindly change the tagline of the website to a different font Segoe UI Semibold since the current font seem to rough and thick. Thanks.

```html
<!DOCTYPE html>
<html lang="en">
<head>
<meta charset="utf-8">
<title>qLumio Stationery</title>
<link href="https://fonts.googleapis.com/css2?family=Exo+2:wght@400;600;800&display=swap" rel="stylesheet">
<style>
:root{
  --bg:#eceef0;
  --paper:#ffffff;
  --blue:#1f3fa8;
  --blue-deep:#0d2378;
  --blue-light:#3f6fd6;
  --green:#7cc23e;
  --ink:#2f3a55;
  --mark:#dfe6ef;
}
*{margin:0;padding:0;box-sizing:border-box}
html,body{width:1200px;height:936px;overflow:hidden;background:var(--bg);font-family:"Exo 2",sans-serif;color:var(--ink)}
.canvas{position:relative;width:1200px;height:936px}
.sheet{position:absolute;background:var(--paper);overflow:hidden;box-shadow:0 3px 10px rgba(0,0,0,.18)}
.sheet svg.wave{position:absolute;left:0;width:100%;display:block}
.brand{position:absolute;display:flex;align-items:center;gap:6px;font-weight:800;color:var(--blue);letter-spacing:.04em;text-transform:uppercase;line-height:1;white-space:nowrap}
.brand .dot{border-radius:50%;background:var(--blue-light);flex:none}
.contact{position:absolute;font-size:6px;line-height:8.5px;color:var(--ink)}
.contact p{white-space:nowrap}

.letterhead{left:178px;top:71px;width:395px;height:540px}
.letterhead .brand{left:24px;top:40px;font-size:26px}
.letterhead .brand .dot{width:15px;height:15px}
.letterhead .contact{left:232px;top:14px}
.letterhead .mark{position:absolute;left:140px;top:215px;width:112px;height:112px;border-radius:50%;background:var(--mark)}

.folder{left:637px;top:38px;width:477px;height:599px}
.folder .brand{left:50%;top:218px;transform:translateX(-50%);flex-direction:column;gap:12px;font-size:58px}
.folder .brand .dot{width:34px;height:34px}

.card{left:43px;width:181px;height:100px}
.card-front{top:662px}
.card-front .brand{left:10px;top:10px;font-size:14px;gap:4px}
.card-front .brand .dot{width:9px;height:9px}
.card-front .person{position:absolute;left:12px;top:32px;line-height:9px}
.card-front .person .name{font-size:8px;font-weight:600;color:var(--blue)}
.card-front .person .role{font-size:6px}
.card-back{top:775px;height:104px;background:linear-gradient(135deg,var(--blue-light),var(--blue-deep))}
.card-back .mark{position:absolute;left:24px;top:22px;width:56px;height:56px;border-radius:50%;background:rgba(255,255,255,.14)}

.envelope-front{left:262px;top:673px;width:441px;height:206px}
.envelope-front .brand{left:18px;top:22px;font-size:28px}
.envelope-front .brand .dot{width:15px;height:15px}
.envelope-front .contact{left:20px;top:58px;font-size:5.5px;line-height:7.5px}

.envelope-back{left:741px;top:673px;width:413px;height:206px}
.envelope-back .site{position:absolute;left:0;right:0;top:28px;text-align:center;color:#fff;font-size:7px;letter-spacing:.4em;font-weight:600}
</style>
</head>
<body>
<div class="canvas">

  <section class="sheet letterhead">
    <svg class="wave" style="top:0;height:50px" viewBox="0 0 100 20" preserveAspectRatio="none">
      <path d="M0 0H18C11 3 5 8 0 14Z" fill="var(--blue)"/>
      <path d="M0 16C7 8 14 3 22 0" fill="none" stroke="var(--green)" stroke-width=".8"/>
    </svg>
    <div class="brand"><span class="dot"></span>qLumio</div>
    <div class="contact">
      <p>Lot C-17, 5B Floor, 8 Kilner Plaza,</p>
      <p>No. 7, Jalan 24/6, 47810 Petaling Jaya</p>
      <p>Selangor, Malaysia</p>
      <p>Tel +60 3 7955 2401</p>
      <p>Fax +60 3 7955 2402</p>
      <p>marissa@qlumiomarketing.example</p>
      <p>www.qlumiomarketing.example</p>
    </div>
    <div class="mark" role="img" aria-label="Brand symbol area"></div>
    <svg class="wave" style="bottom:0;height:120px" viewBox="0 0 100 50" preserveAspectRatio="none">
      <path d="M0 36C30 44 65 30 100 8V50H0Z" fill="var(--blue)"/>
      <path d="M0 32C30 40 65 26 100 3" fill="none" stroke="var(--green)" stroke-width="1.6"/>
      <path d="M0 42C35 50 70 34 100 16V50H0Z" fill="var(--blue-deep)" opacity=".5"/>
    </svg>
  </section>

  <section class="sheet folder">
    <svg class="wave" style="top:0;height:50px" viewBox="0 0 100 12" preserveAspectRatio="none">
      <path d="M0 0H30C18 1 8 4 0 8Z" fill="var(--blue)"/>
      <path d="M0 10C12 3 40 1 100 1" fill="none" stroke="var(--green)" stroke-width=".6"/>
    </svg>
    <div class="brand"><span class="dot"></span>qLumio</div>
    <svg class="wave" style="bottom:0;height:150px" viewBox="0 0 100 40" preserveAspectRatio="none">
      <path d="M0 28C30 38 65 24 100 4V40H0Z" fill="var(--blue)"/>
      <path d="M0 24C30 34 65 20 100 0" fill="none" stroke="var(--green)" stroke-width="1.4"/>
      <path d="M0 34C35 41 70 28 100 13V40H0Z" fill="var(--blue-deep)" opacity=".5"/>
    </svg>
  </section>

  <section class="sheet card card-front">
    <div class="brand"><span class="dot"></span>qLumio</div>
    <div class="person">
      <p class="name">Marissa Tanaka</p>
      <p class="role">Senior Manager</p>
    </div>
    <svg class="wave" style="bottom:0;height:34px" viewBox="0 0 100 30" preserveAspectRatio="none">
      <path d="M0 22C30 28 65 18 100 4V30H0Z" fill="var(--blue)"/>
      <path d="M0 18C30 24 65 14 100 0" fill="none" stroke="var(--green)" stroke-width="1.4"/>
    </svg>
  </section>

  <section class="sheet card card-back">
    <div class="mark" role="img" aria-label="Faint brand symbol"></div>
  </section>

  <section class="sheet envelope-front">
    <div class="brand"><span class="dot"></span>qLumio</div>
    <div class="contact">
      <p>Lot C-17, 5B Floor, 8 Kilner Plaza,</p>
      <p>No. 7, Jalan 24/6, 47810 Petaling Jaya</p>
      <p>Selangor, Malaysia</p>
    </div>
    <svg class="wave" style="bottom:0;height:90px" viewBox="0 0 100 30" preserveAspectRatio="none">
      <path d="M0 20C30 28 65 16 100 4V30H0Z" fill="var(--blue)"/>
      <path d="M0 16C30 24 65 12 100 0" fill="none" stroke="var(--green)" stroke-width="1"/>
    </svg>
  </section>

  <section class="sheet envelope-back">
    <svg class="wave" style="top:0;height:80px" viewBox="0 0 100 30" preserveAspectRatio="none">
      <path d="M0 0H100V22C65 30 35 30 0 20Z" fill="var(--blue)"/>
    </svg>
    <div class="site">WWW.QLUMIOMARKETING.EXAMPLE</div>
  </section>

</div>
</body>
</html>
```